Halvorne apparel business card

We are a clothing manufacturers agent based in London. Our clients are fashion retailers in the UK and Europe. We are looking for a business card design that communicates corporate stability and a creative edge

Target Market(s)

our customers are large international fashion retailers, smaller fashion stores and distributors and designers

Industry/Entity Type

Clothing

```html
<!DOCTYPE html>
<html lang="en">
<head>
<meta charset="utf-8">
<title>Halvorne Apparel — Business Card</title>
<link rel="stylesheet" href="https://fonts.googleapis.com/css2?family=Quicksand:wght@400&display=swap">
<style>
  :root {
    --page-bg: #e6e6e6;
    --card-base: #9b1b4d;
    --card-shadow: #7d1a30;
    --card-ink: #ffffff;
  }
  html, body {
    margin: 0;
    padding: 0;
    width: 1200px;
    height: 1000px;
    overflow: hidden;
    background: var(--page-bg);
  }
  .business-card {
    position: absolute;
    left: 150px;
    top: 209px;
    width: 900px;
    height: 582px;
    background: var(--card-base);
    overflow: hidden;
  }
  .long-shadow {
    position: absolute;
    inset: 0;
    width: 900px;
    height: 582px;
  }
  .long-shadow polygon { fill: var(--card-shadow); }
  .company-name {
    position: absolute;
    left: 85px;
    top: 238px;
    margin: 0;
    font-family: "Quicksand", sans-serif;
    font-weight: 400;
    font-size: 72px;
    line-height: 72px;
    letter-spacing: 0;
    color: var(--card-ink);
    white-space: nowrap;
  }
  .website {
    position: absolute;
    right: 50px;
    top: 488px;
    margin: 0;
    font-family: "Quicksand", sans-serif;
    font-weight: 400;
    font-size: 34px;
    line-height: 40px;
    letter-spacing: -0.5px;
    color: var(--card-ink);
    white-space: nowrap;
  }
</style>
</head>
<body>
  <main class="business-card">
    <svg class="long-shadow" viewBox="0 0 900 582" aria-hidden="true">
      <polygon points="85,303 765,303 900,411 900,582 327,582"/>
    </svg>
    <h1 class="company-name">Halvorne Apparel</h1>
    <p class="website">www.halvorne.com</p>
  </main>
</body>
</html>
```